Home page design for a business selling commercial cleaning machines

We need a home page web design for a wholesale business selling commercial and industrial cleaning machines and spare parts. There is a huge range of products but we don't want the home page to be too cluttered and confusing.
- The design needs to be practical and functional - sharp corners, lots of white with just accents/splashes of the business colours.
- This is a link to their holding page which is very very basic - http://www.vornaspec.co.nz/ - use this to get the accent colours but please use lots and lots more WHITE in the home page design! There are no colour codes available.
- The attached HPID (home page design information) is in table boxes just to see placement of information. Information in orange text. Words to go on the design in black text.
- Expected standard of design examples:
http://brimalo-aquaforce.com/
http://brimalointernational.com/
http://tovesk.com/
http://www.mulfin.wb.gs/ (different industry)
- Only use Google fonts. Non-responsive. Width 1100pixels. Header height (without nav bar) 150-160 pixels.
- Will need a PSD of the chosen homepage design (CS5 compatible)

```html
<!DOCTYPE html>
<html lang="en">
<head>
<meta charset="utf-8">
<title>Vornaspec – Commercial Cleaning Machines</title>
<link rel="stylesheet" href="https://fonts.googleapis.com/css2?family=Open+Sans:wght@400;600;700&display=swap">
<style>
:root{
  --white:#ffffff;
  --ink:#222222;
  --text:#4a4a4a;
  --muted:#8a8a8a;
  --accent:#a5a2a6;
  --accent-dark:#8f8c90;
  --band:#d9d9d9;
  --btn:#3d3d3d;
  --submit:#555555;
  --footer:#5a5a5a;
  --footer-base:#3f3f3f;
  --line:#dcdcdc;
}
*{box-sizing:border-box;margin:0;padding:0}
html,body{width:1200px;height:2225px;overflow:hidden}
body{font-family:"Open Sans",Arial,sans-serif;color:var(--text);background:var(--white);position:relative}
a{color:inherit;text-decoration:none}

.top-rule{position:absolute;left:0;top:0;width:1200px;height:7px;background:var(--accent)}

.site-header{position:absolute;left:0;top:7px;width:1200px;height:131px}
.brand{position:absolute;left:92px;top:52px;display:flex;align-items:center;gap:10px}
.brand-mark{width:14px;height:14px;background:var(--accent-dark)}
.brand-name{font-size:34px;font-weight:700;letter-spacing:2px;color:#6d6d6d}
.header-info{position:absolute;right:94px;top:16px;text-align:right;font-size:12.5px;line-height:26px;color:var(--muted)}
.header-phone{position:absolute;right:300px;top:84px;font-size:21px;color:#8a8a8a}
.search{position:absolute;left:909px;top:82px;width:197px;height:30px;border:1px solid #bdbdbd;display:flex;align-items:center;padding:0 8px;font-size:11px;color:#555}
.search svg{margin-left:auto}

.main-nav{position:absolute;left:0;top:138px;width:1200px;height:49px;background:var(--accent);display:flex;justify-content:center;align-items:center;gap:44px;font-size:12.5px;color:var(--white)}

.hero{position:absolute;left:0;top:187px;width:1200px;height:498px;background:linear-gradient(100deg,#e8e8e6 0%,#f4f4f2 45%,#dedcd8 100%)}
.hero-panel{position:absolute;left:745px;top:0;width:361px;height:498px;background:rgba(120,120,120,.45);padding:26px 16px 0 16px;color:var(--white)}
.hero-panel h2{font-size:22px;font-weight:400;color:#1c1c1c;margin-bottom:14px}
.why-list{list-style:none}
.why-list li{display:flex;gap:14px;font-size:12px;line-height:21px;color:#2b2b2b;margin-bottom:21px}
.why-list svg{flex:none;margin-top:5px}
.hero-dots{position:absolute;right:95px;top:468px;display:flex;gap:6px}
.hero-dots span{width:12px;height:12px;border-radius:50%;border:1px solid #777;background:var(--white)}
.hero-dots span:first-child{background:#ddd}

.section-title{position:absolute;left:0;top:717px;width:1200px;text-align:center;font-size:20px;color:#8a8a8a;letter-spacing:.3px}

.category{position:absolute;top:776px;width:239px;height:241px;border:1px solid var(--line)}
.category .cat-img{height:182px}
.category .cat-label{height:59px;background:var(--accent);color:var(--white);font-size:17px;display:flex;align-items:center;justify-content:center}

.feature{position:absolute;top:1052px;width:323px}
.feature .feat-img{height:197px;border:1px solid var(--line)}
.feature h3{margin-top:18px;font-size:13px;font-weight:400;color:var(--ink);text-transform:uppercase}
.feature p{margin-top:10px;font-size:13.4px;line-height:24.5px;color:var(--text)}
.btn{display:inline-flex;align-items:center;justify-content:center;margin-top:14px;height:33px;padding:0 12px;min-width:116px;background:linear-gradient(#555,#2e2e2e);color:var(--white);font-size:10.5px;font-weight:600;text-transform:uppercase}

.contact-band{position:absolute;left:0;top:1465px;width:1200px;height:279px;background:var(--band)}
.contact-band h2{position:absolute;left:0;top:40px;width:1200px;text-align:center;font-size:16px;font-weight:400;color:var(--ink)}
.field{position:absolute;width:240px;height:54px;background:var(--white);font-size:11.5px;color:#555;display:flex;align-items:center;padding-left:12px}
.submit{position:absolute;left:873px;top:128px;width:186px;height:61px;background:var(--submit);color:var(--white);font-size:17px;display:flex;align-items:center;justify-content:center}

.partners{position:absolute;left:0;top:1744px;width:1200px;height:133px}
.partner{position:absolute;top:46px;height:53px}
.partners .arrow{position:absolute;top:53px}

.site-footer{position:absolute;left:0;top:1877px;width:1200px;height:244px;background:var(--footer);color:var(--white)}
.footer-col{position:absolute;top:24px}
.footer-col h4{font-size:17px;font-weight:400;margin-bottom:12px}
.footer-col ul{list-style:none;font-size:11.5px;line-height:22.5px}
.footer-map{position:absolute;left:685px;top:52px;width:421px;height:162px;background:linear-gradient(135deg,#cfdce8,#e6e2d6 50%,#bcd0e6)}

.base-bar{position:absolute;left:0;top:2121px;width:1200px;height:104px;background:var(--footer-base);color:var(--white)}
.base-links{position:absolute;left:92px;top:26px;font-size:11px}
.base-links b{font-weight:700}
.copyright{position:absolute;left:92px;top:54px;font-size:10.5px}
.base-brand{position:absolute;left:480px;top:30px;font-size:30px;font-weight:700;letter-spacing:2px;color:#c9c9c9}
.social{position:absolute;top:32px;width:28px;height:28px}
</style>
</head>
<body>

<div class="top-rule"></div>

<header class="site-header">
  <a class="brand" href="#"><span class="brand-mark"></span><span class="brand-name">VORNASPEC</span></a>
  <div class="header-info">
    2 / 48 Kereru Rd, Tawanui (office). Open to the public.<br>
    Head office Tawanui Coast | Distributors NZ wide
  </div>
  <div class="header-phone">Call :04 318 5276</div>
  <div class="search">Search
    <svg width="14" height="14" viewBox="0 0 14 14"><circle cx="6" cy="6" r="4.5" fill="none" stroke="#111" stroke-width="1.8"/><line x1="9.3" y1="9.3" x2="13" y2="13" stroke="#111" stroke-width="2"/></svg>
  </div>
</header>

<nav class="main-nav">
  <a href="#">Home</a><a href="#">About</a><a href="#">Water blasters</a><a href="#">Drain cleaners</a><a href="#">Custom machines</a><a href="#">Vacuum Cleaners</a><a href="#">Pumps</a><a href="#">Quote</a><a href="#">Contact Us</a>
</nav>

<section class="hero" role="img" aria-label="Photo of a person vacuuming a bright living room">
  <div class="hero-panel">
    <h2>Why Choose Vornaspec?</h2>
    <ul class="why-list">
      <li><svg width="12" height="10" viewBox="0 0 12 10"><path d="M1 5l3.5 3.5L11 1" fill="none" stroke="#111" stroke-width="2"/></svg>High quality Italian cleaning machines</li>
      <li><svg width="12" height="10" viewBox="0 0 12 10"><path d="M1 5l3.5 3.5L11 1" fill="none" stroke="#111" stroke-width="2"/></svg>Wide range of brands and models</li>
      <li><svg width="12" height="10" viewBox="0 0 12 10"><path d="M1 5l3.5 3.5L11 1" fill="none" stroke="#111" stroke-width="2"/></svg>Specialist knowledge &amp; expert advice</li>
      <li><svg width="12" height="10" viewBox="0 0 12 10"><path d="M1 5l3.5 3.5L11 1" fill="none" stroke="#111" stroke-width="2"/></svg>Cost of machines – more affordable for top quality</li>
      <li><svg width="12" height="10" viewBox="0 0 12 10"><path d="M1 5l3.5 3.5L11 1" fill="none" stroke="#111" stroke-width="2"/></svg>Able to service and repair all types of cleaning machines</li>
      <li><svg width="12" height="10" viewBox="0 0 12 10"><path d="M1 5l3.5 3.5L11 1" fill="none" stroke="#111" stroke-width="2"/></svg>Huge range of affordable spare parts</li>
      <li><svg width="12" height="10" viewBox="0 0 12 10"><path d="M1 5l3.5 3.5L11 1" fill="none" stroke="#111" stroke-width="2"/></svg>Distributors nationwide offering excellent sales &amp; service support</li>
      <li><svg width="12" height="10" viewBox="0 0 12 10"><path d="M1 5l3.5 3.5L11 1" fill="none" stroke="#111" stroke-width="2"/></svg>Great family business with excellent customer service for over 24 years!</li>
    </ul>
  </div>
  <div class="hero-dots"><span></span><span></span><span></span></div>
</section>

<h2 class="section-title">HUGE RANGE OF QUALITY CLEANING MACHINES</h2>

<a class="category" style="left:92px" href="#"><div class="cat-img" role="img" aria-label="Petrol water blaster on a wheeled frame" style="background:radial-gradient(circle at 50% 55%,#d9d0cc,#fff 70%)"></div><div class="cat-label">Water Blasters</div></a>
<a class="category" style="left:350px" href="#"><div class="cat-img" role="img" aria-label="Bottles of drain cleaning fluid" style="background:radial-gradient(circle at 50% 50%,#dfe8d6,#fff 70%)"></div><div class="cat-label">Drain Cleaners</div></a>
<a class="category" style="left:610px" href="#"><div class="cat-img" role="img" aria-label="Canister vacuum cleaner" style="background:radial-gradient(circle at 50% 60%,#cfd5df,#fff 70%)"></div><div class="cat-label">Custom machines</div></a>
<a class="category" style="left:868px" href="#"><div class="cat-img" role="img" aria-label="Handheld vacuum cleaner" style="background:radial-gradient(circle at 50% 50%,#dedede,#fff 70%)"></div><div class="cat-label">Vacuum Cleaners</div></a>

<article class="feature" style="left:92px">
  <div class="feat-img" role="img" aria-label="Vacuum cleaner on a shaggy rug" style="background:linear-gradient(160deg,#b7a58c,#6c5844 60%,#c8c2b8)"></div>
  <h3>Huge range of quality cleaning machines</h3>
  <p>Lorem ipsum dolor sit amet, consectetuer adipiscing elit. Aenean commodo ligula eget dolor. Aenean massa. Cum sociis natoque penatibus et magnis dis parturient montes, nascetur ridiculus mus.</p>
  <a class="btn" href="#">Request quote</a>
</article>
<article class="feature" style="left:439px">
  <div class="feat-img" role="img" aria-label="Map of New Zealand" style="background:linear-gradient(120deg,#a9d6ea,#cfe4b8 45%,#a9d6ea 75%)"></div>
  <h3>Nationwide distributors for sales &amp; servicing</h3>
  <p>Lorem ipsum dolor sit amet, consectetuer adipiscing elit. Aenean commodo ligula eget dolor. Aenean massa. Cum sociis natoque penatibus et magnis dis parturient montes, nascetur ridiculus mus.</p>
  <a class="btn" href="#">Contact map</a>
</article>
<article class="feature" style="left:782px">
  <div class="feat-img" role="img" aria-label="Brass gear spare parts" style="background:linear-gradient(135deg,#3a3532,#a08a6a 50%,#5a5450)"></div>
  <h3>Comprehensive range of spare parts</h3>
  <p>Lorem ipsum dolor sit amet, consectetuer adipiscing elit. Aenean commodo ligula eget dolor. Aenean massa. Cum sociis natoque penatibus et magnis dis parturient montes, nascetur ridiculus mus.</p>
  <a class="btn" href="#">Spare parts</a>
</article>

<section class="contact-band">
  <h2>Would you like a Vornaspec representative to contact you? Please fill the in the form and we'll be in touch very soon</h2>
  <div class="field" style="left:92px;top:92px">First name</div>
  <div class="field" style="left:347px;top:92px">Last name</div>
  <div class="field" style="left:605px;top:92px">Phone</div>
  <div class="field" style="left:92px;top:169px">Email Address:</div>
  <div class="field" style="left:347px;top:169px">Area you live in</div>
  <div class="field" style="left:605px;top:169px">Any further details?</div>
  <div class="submit">Submit</div>
</section>

<section class="partners" aria-label="Brands we supply">
  <svg class="arrow" style="left:34px" width="22" height="34" viewBox="0 0 22 34"><path d="M18 2L4 17l14 15" fill="none" stroke="#9a9a9a" stroke-width="6"/></svg>
  <div class="partner" style="left:88px;width:200px;background:#f0f0f0"></div>
  <div class="partner" style="left:333px;width:213px;background:#e7e7e7"></div>
  <div class="partner" style="left:587px;width:103px;background:#3c6f8f"></div>
  <div class="partner" style="left:726px;width:93px;background:#c6d4ea"></div>
  <div class="partner" style="left:860px;width:246px;background:#2b2b2b"></div>
  <svg class="arrow" style="left:1128px" width="22" height="34" viewBox="0 0 22 34"><path d="M4 2l14 15L4 32" fill="none" stroke="#9a9a9a" stroke-width="6"/></svg>
</section>

<footer class="site-footer">
  <div class="footer-col" style="left:90px"><h4>Links</h4><ul><li>Home</li><li>About</li><li>Meet the Team</li><li>Testimonials</li><li>FAQ</li><li>Quote</li></ul></div>
  <div class="footer-col" style="left:230px"><h4>Water Blasters</h4><ul><li>Hot water blasters</li><li>Cold water blasters electric</li><li>Cold water blasters petrol or diesel</li><li>Steam water blasters</li></ul></div>
  <div class="footer-col" style="left:480px"><h4>Vacuum Cleaners</h4><ul><li>Shampoo machines</li><li>Pumps high pressure</li><li>Spare Parts</li><li>PTO machines</li></ul></div>
  <div class="footer-col" style="left:685px"><h4>Contact/Map</h4></div>
  <div class="footer-map" role="img" aria-label="Road map of the South Island showing office location"></div>
</footer>

<div class="base-bar">
  <div class="base-links">Home &nbsp;|&nbsp; About Us &nbsp;|&nbsp; Services &nbsp;|&nbsp; <b>News/Blog</b> &nbsp;|&nbsp; <b>Contact Us</b></div>
  <div class="copyright">© Copyrights 2014 Vornaspec. All rights reserved</div>
  <div class="base-brand">VORNASPEC</div>
  <div class="social" style="left:938px;background:#3b5a98"></div>
  <div class="social" style="left:985px;background:#2aa3d8"></div>
  <div class="social" style="left:1032px;background:#6a6a6a"></div>
  <div class="social" style="left:1078px;background:#1f6fa6"></div>
</div>

</body>
</html>
```